KORVAL RENOVATIONS AND CUSTOM BUILDS

5pages:
Home/ who we are , services offered, why us,
recent projects/ gallery , contact us

Industry/Entity Type

Design, renovations, project management

Coding

Coded - Design and coding required

Number of Pages Required

5+ page

Requirements
Should not have
• Too many colours

```html
<!DOCTYPE html>
<html lang="en">
<head>
<meta charset="utf-8">
<title>Korval Renovations and Custom Builds</title>
<link rel="stylesheet" href="https://fonts.googleapis.com/css2?family=Poppins:wght@300;400;500;600;700;800&display=swap">
<style>
:root{
  --green:#79b52b;
  --green-dark:#5f9620;
  --navy:#1c2b4f;
  --ink:#1e1e1e;
  --dark:#191919;
  --teal:#5cc4bb;
  --grey:#6b6b6b;
  --light:#eef0f2;
  --white:#ffffff;
  --pin:#e0302b;
}
*{box-sizing:border-box;margin:0;padding:0}
html,body{width:1200px;height:5199px;overflow:hidden}
body{font-family:'Poppins',sans-serif;color:var(--ink);background:var(--white);position:relative}
.section{position:absolute;left:0;width:1200px}
.abs{position:absolute}
.photo{position:absolute}
.h-bold{font-weight:800}
.h-light{font-weight:300}
svg{display:block}

.topbar{top:0;height:30px;font-size:12px;color:var(--grey)}
.topbar .item{position:absolute;top:7px;display:flex;align-items:center;gap:6px}
.header{top:30px;height:70px}
.logo{position:absolute;display:flex;align-items:center;gap:10px}
.logo .mark{width:14px;height:14px;background:var(--green);flex:none}
.logo .name{font-weight:700;color:var(--navy);line-height:1.05}
.nav{position:absolute;left:373px;top:8px;width:827px;height:52px}
.nav .home{position:absolute;left:0;top:0;width:135px;height:52px;background:var(--green);clip-path:polygon(22px 0,100% 0,100% 100%,0 100%)}
.nav .bar{position:absolute;left:121px;top:0;right:0;height:52px;background:var(--navy)}
.nav a{position:absolute;top:17px;color:var(--white);font-size:13px;font-weight:500;text-decoration:none;white-space:nowrap}

.hero{top:100px;height:512px;background:#eceef0}
.hero-photo{left:0;top:0;width:1200px;height:512px;background:
  radial-gradient(ellipse 180px 150px at 700px 250px,#ffffff 0%,rgba(255,255,255,0) 100%),
  linear-gradient(90deg,#f1f2f4 0%,#e8ebee 45%,#c4cbd3 68%,#55627a 82%,#1f2940 100%)}
.hero h1{position:absolute;left:70px;top:112px;font-weight:800;color:var(--navy);font-size:38px;line-height:49px;text-transform:uppercase}
.hero h1 .brand{display:block;color:var(--green);font-size:56px;line-height:62px}
.hero p{position:absolute;left:70px;top:283px;width:360px;font-size:15px;line-height:26px;color:#333}
.btn{position:absolute;display:flex;align-items:center;gap:14px;background:var(--navy);color:var(--white);border-radius:24px;font-size:11px;font-weight:600;text-transform:uppercase;padding:0 6px 0 16px;height:40px;box-shadow:0 6px 14px rgba(0,0,0,.2);white-space:nowrap}
.btn .arrow{width:28px;height:28px;border-radius:50%;background:var(--white);display:flex;align-items:center;justify-content:center}
.dots{position:absolute;left:575px;top:477px;display:flex;gap:6px}
.dots i{width:11px;height:11px;border-radius:50%;border:1.5px solid var(--green)}
.dots i.on{background:var(--green)}

.about{top:612px;height:854px}
.frame{position:absolute;border:6px solid var(--green);border-radius:3px;background:var(--white)}
.frame.teal{border-color:var(--teal)}
.infobox{position:absolute;background:var(--dark);color:var(--white);padding:0 40px}
.infobox h2{font-size:27px;letter-spacing:.5px;margin-bottom:18px}
.infobox p{font-size:14px;line-height:25px}
.stripes{position:absolute;width:140px;height:70px}

.services{top:1466px;height:702px;background:var(--navy)}
.sec-title{font-size:32px;text-transform:uppercase;letter-spacing:.3px}
.services .sec-title{position:absolute;top:60px;width:1200px;text-align:center;color:var(--white)}
.card{position:absolute;width:247px;height:217px;background:var(--white);border-radius:6px;overflow:hidden}
.card .pic{position:absolute;left:0;top:0;width:247px;height:160px}
.card .label{position:absolute;left:12px;top:160px;width:170px;height:57px;display:flex;align-items:center;font-size:12px;font-weight:600;line-height:16px}
.card .ico{position:absolute;right:0;top:160px;width:68px;height:57px;background:var(--green);display:flex;align-items:center;justify-content:center}

.means{top:2168px;height:656px}
.shot{position:absolute;border:6px solid var(--white);box-shadow:0 4px 16px rgba(0,0,0,.18);border-radius:4px;overflow:hidden}
.means .sec-title{position:absolute;left:668px;top:72px;color:var(--navy);line-height:40px}
.col-head{position:absolute;top:173px;font-size:14px;font-weight:600;color:var(--green);text-transform:uppercase}
.ticks{position:absolute;top:205px;list-style:none;font-size:14px;color:#333}
.ticks li{height:34.5px;display:flex;align-items:center;gap:12px}

.why{top:2824px;height:581px;background:var(--dark)}
.why .sec-title{position:absolute;left:70px;top:74px;color:var(--white)}
.why-item{position:absolute;left:70px;width:420px;height:60px;display:flex;align-items:center;gap:30px;border-bottom:1px solid #4a4a4a;color:var(--white);font-size:20px}
.why-item.last{border-bottom:none}
.why-item .circ{width:52px;height:52px;border-radius:50%;background:var(--green);display:flex;align-items:center;justify-content:center;flex:none}

.area{top:3405px;height:518px}
.area .sec-title{position:absolute;left:79px;top:210px;color:var(--navy)}
.pills{position:absolute;left:77px;top:284px;width:389px;height:44px;border-radius:22px;background:var(--white);box-shadow:0 4px 14px rgba(0,0,0,.12);display:flex;align-items:center;gap:26px;padding-left:26px;font-size:15px;color:#333}
.pills span{display:flex;align-items:center;gap:7px}
.map-panel{left:599px;top:18px;width:524px;height:460px;border-radius:18px;background:linear-gradient(160deg,#f4f5f6 0%,#e4e7ea 100%);border:1px solid #d9dcdf}

.contact{top:3923px;height:605px}
.contact-bg{left:0;top:0;width:1200px;height:605px;background:linear-gradient(90deg,#f0f2f4 0%,#2f5ea8 10%,#244f95 28%,#3a3a3a 42%,#242424 70%,#1b1b1b 100%)}
.form-card{position:absolute;left:460px;top:103px;width:488px;height:411px;background:var(--white);border-radius:6px;box-shadow:0 10px 30px rgba(0,0,0,.2)}
.form-card .sec-title{position:absolute;left:37px;top:55px;color:var(--navy)}
.field{position:absolute;left:37px;width:308px;border-bottom:1px solid #888;font-size:11px;color:#333;padding-bottom:6px}
.info-box{position:absolute;left:841px;top:170px;width:270px;height:340px;background:var(--green);color:var(--white)}
.info-row{position:absolute;left:30px;display:flex;align-items:center;gap:14px;font-size:15px;line-height:22px;white-space:nowrap}
.info-row .c{width:38px;height:38px;border-radius:50%;background:var(--white);display:flex;align-items:center;justify-content:center;flex:none}
.tab{position:absolute;height:12px;background:var(--green);border-radius:6px}

.newsletter{top:4528px;height:210px;background:var(--green)}
.newsletter .sec-title{position:absolute;left:107px;top:82px;color:var(--white);line-height:42px}
.sub-box{position:absolute;left:510px;top:79px;width:569px;height:61px;background:var(--white);border-radius:6px;box-shadow:0 6px 18px rgba(0,0,0,.15)}
.sub-box .ph{position:absolute;left:22px;top:20px;font-size:15px;color:#333}
.sub-box .btn{right:20px;top:11px;height:40px}

.footer{top:4738px;height:461px;background:var(--dark);color:var(--white)}
.f-head{position:absolute;top:66px;font-size:15px;font-weight:700;color:var(--green);text-transform:uppercase}
.f-list{position:absolute;top:113px;list-style:none;font-size:11px}
.f-list li{height:28px;display:flex;align-items:center;gap:12px;white-space:nowrap}
.social{position:absolute;left:70px;top:212px;display:flex;gap:12px}
.social i{width:32px;height:32px;border-radius:50%;border:1.5px solid #888;display:block}
.thumb{position:absolute;width:86px;height:67px}
.f-line{position:absolute;left:70px;top:377px;width:1057px;height:1px;background:#444}
.copy{position:absolute;top:400px;width:1200px;text-align:center;font-size:11px}
.copy b{color:var(--green);font-weight:400}
.up{position:absolute;left:1093px;top:359px;width:34px;height:34px;border-radius:50%;background:var(--green);display:flex;align-items:center;justify-content:center}
</style>
</head>
<body>

<div class="section topbar">
  <div class="item" style="left:74px">
    <svg width="12" height="12" viewBox="0 0 24 24"><path fill="#79b52b" d="M6.6 10.8a15 15 0 006.6 6.6l2.2-2.2a1 1 0 011-.25 11 11 0 003.6.6 1 1 0 011 1V20a1 1 0 01-1 1A17 17 0 013 4a1 1 0 011-1h3.5a1 1 0 011 1 11 11 0 00.6 3.6 1 1 0 01-.25 1z"/></svg>
    <span>CALL US FOR HELP!+ (555) 014 2290</span>
  </div>
  <div class="item" style="left:820px">
    <svg width="11" height="13" viewBox="0 0 24 28"><path fill="#79b52b" d="M12 0a10 10 0 00-10 10c0 7.5 10 18 10 18s10-10.5 10-18A10 10 0 0012 0zm0 14a4 4 0 110-8 4 4 0 010 8z"/></svg>
    <span>OUR LOCATION : 48 Alder Lane, Canada</span>
  </div>
</div>

<header class="section header">
  <div class="logo" style="left:70px;top:20px">
    <span class="mark"></span>
    <div class="name"><div style="font-size:15px">KORVAL RENOVATIONS</div><div style="font-size:9px;letter-spacing:1.6px">AND CUSTOM BUILDS</div></div>
  </div>
  <nav class="nav">
    <div class="home"></div>
    <div class="bar"></div>
    <a style="left:34px;display:flex;gap:6px;align-items:center;top:16px"><svg width="14" height="14" viewBox="0 0 24 24"><path fill="none" stroke="#fff" stroke-width="2" d="M3 11l9-8 9 8v10h-6v-6H9v6H3z"/></svg>Home</a>
    <a style="left:141px">Who we are</a>
    <a style="left:250px">Services offered</a>
    <a style="left:387px">Why us</a>
    <a style="left:472px">Recent projects</a>
    <a style="left:605px">Gallery</a>
    <a style="left:685px">Contact us</a>
  </nav>
</header>

<section class="section hero">
  <div class="photo hero-photo" role="img" aria-label="Business person in a dark suit holding a small white wireframe house model"></div>
  <h1><span class="brand">KORVAL</span>Renovations and<br>Custom Builds</h1>
  <p>A team of professionals with over 25 years of combined experience</p>
  <div class="btn" style="left:70px;top:347px">Contact us<span class="arrow"><svg width="14" height="14" viewBox="0 0 24 24"><path fill="none" stroke="#1c2b4f" stroke-width="2.5" d="M4 12h15M13 6l6 6-6 6"/></svg></span></div>
  <div class="dots"><i class="on"></i><i></i><i></i></div>
</section>

<section class="section about">
  <div class="frame" style="left:70px;top:98px;width:428px;height:585px">
    <div class="photo" role="img" aria-label="Electrician in a white hard hat installing sockets in a white brick wall" style="inset:0;background:linear-gradient(180deg,#f2f2f0 0%,#d9d9d6 40%,#c7a98a 60%,#2f3d5e 85%,#3a4867 100%)"></div>
  </div>
  <div class="infobox" style="left:125px;top:483px;width:464px;height:293px;padding-top:85px">
    <svg class="stripes" style="right:10px;top:22px" viewBox="0 0 140 70"><polygon points="10,55 70,15 70,45 10,70" fill="#79b52b"/><polygon points="78,40 135,5 135,20 78,55" fill="#5cc4bb"/></svg>
    <h2><span class="h-bold">WHO WE</span> <span class="h-light">ARE</span></h2>
    <p>A team of professionals with over 25 years of combined experience in all sectors of the building field with design, trades, and construction management</p>
  </div>

  <div class="frame teal" style="left:613px;top:189px;width:426px;height:587px">
    <div class="photo" role="img" aria-label="Carpenter in a blue shirt drilling into a timber floor" style="left:0;top:202px;width:414px;height:373px;background:linear-gradient(180deg,#9fb6c9 0%,#6d86a5 35%,#d9c4a0 60%,#e6d5b6 100%)"></div>
  </div>
  <div class="infobox" style="left:664px;top:98px;width:464px;height:293px;padding-top:92px">
    <svg class="stripes" style="right:10px;top:2px" viewBox="0 0 140 70"><polygon points="10,55 70,15 70,45 10,70" fill="#79b52b"/><polygon points="78,40 135,5 135,20 78,55" fill="#5cc4bb"/></svg>
    <h2><span class="h-bold">WHAT WE</span> <span class="h-light">DO</span></h2>
    <p>We design, execute, and manage any construction project whether it’s residential, commercial, or institutional</p>
  </div>
</section>

<section class="section services">
  <h2 class="sec-title"><span class="h-bold">SERVICES WE</span> <span class="h-light">OFFER</span></h2>

  <div class="card" style="left:70px;top:140px"><div class="pic" role="img" aria-label="Finished basement with grey walls and wood floor" style="background:linear-gradient(180deg,#e4e4e2 0%,#cfcfcc 55%,#6e6a64 75%,#4e4a45 100%)"></div><div class="label">Finishing Basements</div><div class="ico"><svg width="30" height="30" viewBox="0 0 24 24" fill="none" stroke="#fff" stroke-width="1.5"><path d="M3 11l9-8 9 8v10H3z"/><path d="M8 14h8M8 17h8"/></svg></div></div>
  <div class="card" style="left:341px;top:140px"><div class="pic" role="img" aria-label="Worker fitting a legal second unit" style="background:linear-gradient(180deg,#b9b2a6 0%,#8e877c 45%,#c9b391 75%,#a58a63 100%)"></div><div class="label">Second legal units</div><div class="ico"><svg width="30" height="30" viewBox="0 0 24 24" fill="none" stroke="#fff" stroke-width="1.5"><path d="M3 11l9-8 9 8v10H3z"/><path d="M9 21v-6h6v6"/></svg></div></div>
  <div class="card" style="left:611px;top:140px"><div class="pic" role="img" aria-label="Modern house model with a drafting pen" style="background:linear-gradient(180deg,#5d82b8 0%,#9ab5d6 45%,#eef0f3 75%,#ffffff 100%)"></div><div class="label">Complete Remodeling</div><div class="ico"><svg width="30" height="30" viewBox="0 0 24 24" fill="none" stroke="#fff" stroke-width="1.5"><path d="M3 11l9-8 9 8v10H3z"/><circle cx="12" cy="14" r="3"/></svg></div></div>
  <div class="card" style="left:881px;top:140px"><div class="pic" role="img" aria-label="Bright extension with a red sofa" style="background:linear-gradient(180deg,#f4f4f4 0%,#e2e2e2 55%,#c83a2e 75%,#e8e8e8 100%)"></div><div class="label">Extensions / Additions</div><div class="ico"><svg width="30" height="30" viewBox="0 0 24 24" fill="none" stroke="#fff" stroke-width="1.5"><rect x="4" y="4" width="7" height="7"/><rect x="13" y="13" width="7" height="7"/><path d="M11 7.5h5v5"/></svg></div></div>

  <div class="card" style="left:70px;top:396px"><div class="pic" role="img" aria-label="Navy kitchen with pendant lights" style="background:linear-gradient(180deg,#3c4e6b 0%,#2a3a55 50%,#22314b 75%,#8a7560 100%)"></div><div class="label">Kitchen Renovations</div><div class="ico"><svg width="30" height="30" viewBox="0 0 24 24" fill="none" stroke="#fff" stroke-width="1.5"><rect x="3" y="10" width="18" height="11"/><path d="M3 14h18M12 10v11M7 3v4M17 3v4"/></svg></div></div>
  <div class="card" style="left:341px;top:396px"><div class="pic" role="img" aria-label="Tiler using a laser level on a marble bathroom wall" style="background:linear-gradient(90deg,#3a3a3a 0%,#5b6b4a 30%,#ecebe8 55%,#f4f3f1 100%)"></div><div class="label">Bathroom Renovations</div><div class="ico"><svg width="30" height="30" viewBox="0 0 24 24" fill="none" stroke="#fff" stroke-width="1.5"><path d="M3 12h18v3a5 5 0 01-5 5H8a5 5 0 01-5-5zM6 12V5a2 2 0 014 0"/></svg></div></div>
  <div class="card" style="left:611px;top:396px"><div class="pic" role="img" aria-label="Hand holding a phone over house plans" style="background:linear-gradient(180deg,#e9e9e9 0%,#cfcfcf 50%,#b8a08a 75%,#dedede 100%)"></div><div class="label">Custom Homes</div><div class="ico"><svg width="30" height="30" viewBox="0 0 24 24" fill="none" stroke="#fff" stroke-width="1.5"><circle cx="12" cy="12" r="8"/><path d="M8 13l4-4 4 4v4H8z"/></svg></div></div>
  <div class="card" style="left:881px;top:396px"><div class="pic" role="img" aria-label="Office interior with a wooden desk and chairs" style="background:linear-gradient(180deg,#f3f2ee 0%,#e7e3da 50%,#b8946a 75%,#d9d3c8 100%)"></div><div class="label">Office and Commercial Renovations</div><div class="ico"><svg width="30" height="30" viewBox="0 0 24 24" fill="none" stroke="#fff" stroke-width="1.5"><path d="M3 11l9-8 9 8v10H3z"/><rect x="9" y="13" width="6" height="8"/></svg></div></div>
</section>

<section class="section means">
  <div class="shot" style="left:70px;top:61px;width:539px;height:258px"><div class="photo" role="img" aria-label="Tradesman fitting a cabinet beside an exposed brick wall" style="inset:0;background:linear-gradient(90deg,#e8e6e1 0%,#d4cfc6 30%,#3d4356 55%,#b26a45 75%,#9a5535 100%)"></div></div>
  <div class="shot" style="left:70px;top:343px;width:262px;height:256px"><div class="photo" role="img" aria-label="Worker on a ladder fitting a ceiling" style="inset:0;background:linear-gradient(180deg,#f1f1ef 0%,#dcdcda 45%,#c67a4a 60%,#5b6f8c 85%,#d8d8d6 100%)"></div></div>
  <div class="shot" style="left:349px;top:343px;width:260px;height:256px"><div class="photo" role="img" aria-label="Hand taping a drywall corner" style="inset:0;background:linear-gradient(90deg,#2f2f31 0%,#4a4a4c 35%,#b9b9b6 55%,#d4d4d1 100%)"></div></div>

  <h2 class="sec-title"><span class="h-bold">WHAT THIS REALLY</span><br><span class="h-light">MEANS</span></h2>
  <div class="col-head" style="left:668px">Our team does</div>
  <div class="col-head" style="left:898px">Our subcontractors do</div>
  <ul class="ticks" style="left:668px">
    <li><svg width="15" height="15" viewBox="0 0 24 24" fill="none" stroke="#79b52b" stroke-width="2"><circle cx="12" cy="12" r="10"/><path d="M7 12l3 3 7-7"/></svg>Demolition</li>
    <li><svg width="15" height="15" viewBox="0 0 24 24" fill="none" stroke="#79b52b" stroke-width="2"><circle cx="12" cy="12" r="10"/><path d="M7 12l3 3 7-7"/></svg>Cutting doors/ windows</li>
    <li><svg width="15" height="15" viewBox="0 0 24 24" fill="none" stroke="#79b52b" stroke-width="2"><circle cx="12" cy="12" r="10"/><path d="M7 12l3 3 7-7"/></svg>Framing</li>
    <li><svg width="15" height="15" viewBox="0 0 24 24" fill="none" stroke="#79b52b" stroke-width="2"><circle cx="12" cy="12" r="10"/><path d="M7 12l3 3 7-7"/></svg>Thermal insulation</li>
    <li><svg width="15" height="15" viewBox="0 0 24 24" fill="none" stroke="#79b52b" stroke-width="2"><circle cx="12" cy="12" r="10"/><path d="M7 12l3 3 7-7"/></svg>Fire separation</li>
    <li><svg width="15" height="15" viewBox="0 0 24 24" fill="none" stroke="#79b52b" stroke-width="2"><circle cx="12" cy="12" r="10"/><path d="M7 12l3 3 7-7"/></svg>Drywalling</li>
    <li><svg width="15" height="15" viewBox="0 0 24 24" fill="none" stroke="#79b52b" stroke-width="2"><circle cx="12" cy="12" r="10"/><path d="M7 12l3 3 7-7"/></svg>Painting</li>
    <li><svg width="15" height="15" viewBox="0 0 24 24" fill="none" stroke="#79b52b" stroke-width="2"><circle cx="12" cy="12" r="10"/><path d="M7 12l3 3 7-7"/></svg>Flooring</li>
    <li><svg width="15" height="15" viewBox="0 0 24 24" fill="none" stroke="#79b52b" stroke-width="2"><circle cx="12" cy="12" r="10"/><path d="M7 12l3 3 7-7"/></svg>Doors</li>
    <li><svg width="15" height="15" viewBox="0 0 24 24" fill="none" stroke="#79b52b" stroke-width="2"><circle cx="12" cy="12" r="10"/><path d="M7 12l3 3 7-7"/></svg>Trims</li>
    <li><svg width="15" height="15" viewBox="0 0 24 24" fill="none" stroke="#79b52b" stroke-width="2"><circle cx="12" cy="12" r="10"/><path d="M7 12l3 3 7-7"/></svg>Kitchen cabinets</li>
  </ul>
  <ul class="ticks" style="left:898px">
    <li><svg width="15" height="15" viewBox="0 0 24 24" fill="none" stroke="#79b52b" stroke-width="2"><circle cx="12" cy="12" r="10"/><path d="M7 12l3 3 7-7"/></svg>Plumbing</li>
    <li><svg width="15" height="15" viewBox="0 0 24 24" fill="none" stroke="#79b52b" stroke-width="2"><circle cx="12" cy="12" r="10"/><path d="M7 12l3 3 7-7"/></svg>Electrical</li>
    <li><svg width="15" height="15" viewBox="0 0 24 24" fill="none" stroke="#79b52b" stroke-width="2"><circle cx="12" cy="12" r="10"/><path d="M7 12l3 3 7-7"/></svg>Taping, and</li>
    <li><svg width="15" height="15" viewBox="0 0 24 24" fill="none" stroke="#79b52b" stroke-width="2"><circle cx="12" cy="12" r="10"/><path d="M7 12l3 3 7-7"/></svg>Tiling</li>
  </ul>
</section>

<section class="section why">
  <h2 class="sec-title"><span class="h-bold">WHY</span> <span class="h-light">US</span></h2>
  <div class="why-item" style="top:149px"><span class="circ"><svg width="24" height="24" viewBox="0 0 24 24" fill="none" stroke="#fff" stroke-width="1.6"><rect x="4" y="5" width="16" height="14" rx="2"/><path d="M8 10h8M8 14h5"/></svg></span>Competitive Rates</div>
  <div class="why-item" style="top:222px"><span class="circ"><svg width="24" height="24" viewBox="0 0 24 24" fill="none" stroke="#fff" stroke-width="1.6"><rect x="6" y="3" width="12" height="18" rx="1"/><path d="M9 8h6M9 12h6M9 16h3"/></svg></span>Licensed subcontractors</div>
  <div class="why-item" style="top:296px"><span class="circ"><svg width="24" height="24" viewBox="0 0 24 24" fill="none" stroke="#fff" stroke-width="1.6"><path d="M3 5h12v8H8l-3 3v-3H3zM17 9h4v8h-2v3l-3-3h-5v-2"/></svg></span>Wide network of consultants</div>
  <div class="why-item" style="top:369px"><span class="circ"><svg width="24" height="24" viewBox="0 0 24 24" fill="none" stroke="#fff" stroke-width="1.6"><circle cx="12" cy="12" r="8"/><path d="M12 7v10M9 9.5h4.5a1.8 1.8 0 010 3.5h-3a1.8 1.8 0 000 3.5H15"/></svg></span>Suppliers list suits every budget</div>
  <div class="why-item last" style="top:444px"><span class="circ"><svg width="24" height="24" viewBox="0 0 24 24" fill="none" stroke="#fff" stroke-width="1.6"><rect x="4" y="5" width="16" height="15" rx="1"/><path d="M4 10h16M8 3v4M16 3v4"/></svg></span>Flexible working hours</div>

  <div class="abs" style="left:559px;top:87px;width:289px;height:415px;border:4px solid var(--green)"><div class="photo" role="img" aria-label="Hallway with exposed timber framing before renovation" style="inset:0;background:linear-gradient(90deg,#c9a978 0%,#ead7b3 20%,#6b5a4a 45%,#8c7a68 60%,#e3cca3 80%,#b89363 100%)"></div></div>
  <div class="abs" style="left:845px;top:87px;width:285px;height:415px;border:4px solid var(--teal)"><div class="photo" role="img" aria-label="Finished hallway with white walls and dark floor after renovation" style="inset:0;background:linear-gradient(180deg,#eeece8 0%,#e2ded7 50%,#6e5848 78%,#4e3d31 100%)"></div></div>
  <div class="abs" style="left:815px;top:264px;width:60px;height:60px;border-radius:50%;background:var(--white);display:flex;align-items:center;justify-content:center"><svg width="28" height="28" viewBox="0 0 24 24" fill="none" stroke="#1c2b4f" stroke-width="2.2"><path d="M4 8h15l-4-4M20 16H5l4 4"/></svg></div>
</section>

<section class="section area">
  <h2 class="sec-title"><span class="h-bold">AREA WE</span> <span class="h-light">COVER</span></h2>
  <div class="pills">
    <span><svg width="12" height="15" viewBox="0 0 24 28"><path fill="#1e1e1e" d="M12 0a10 10 0 00-10 10c0 7.5 10 18 10 18s10-10.5 10-18A10 10 0 0012 0zm0 14a4 4 0 110-8 4 4 0 010 8z"/></svg>Oakville</span>
    <span><svg width="12" height="15" viewBox="0 0 24 28"><path fill="#1e1e1e" d="M12 0a10 10 0 00-10 10c0 7.5 10 18 10 18s10-10.5 10-18A10 10 0 0012 0zm0 14a4 4 0 110-8 4 4 0 010 8z"/></svg>Bowmanville</span>
    <span><svg width="12" height="15" viewBox="0 0 24 28"><path fill="#1e1e1e" d="M12 0a10 10 0 00-10 10c0 7.5 10 18 10 18s10-10.5 10-18A10 10 0 0012 0zm0 14a4 4 0 110-8 4 4 0 010 8z"/></svg>Barrie</span>
  </div>
  <div class="photo map-panel" role="img" aria-label="Outline map of Canada with service locations marked in Ontario and the east"></div>
  <svg class="abs" style="left:956px;top:360px" width="26" height="32" viewBox="0 0 24 28"><path fill="#e0302b" d="M12 0a10 10 0 00-10 10c0 7.5 10 18 10 18s10-10.5 10-18A10 10 0 0012 0zm0 14a4 4 0 110-8 4 4 0 010 8z"/></svg>
  <svg class="abs" style="left:1082px;top:300px" width="26" height="32" viewBox="0 0 24 28"><path fill="#e0302b" d="M12 0a10 10 0 00-10 10c0 7.5 10 18 10 18s10-10.5 10-18A10 10 0 0012 0zm0 14a4 4 0 110-8 4 4 0 010 8z"/></svg>
</section>

<section class="section contact">
  <div class="photo contact-bg" role="img" aria-label="Smiling worker in a blue uniform and cap giving a thumbs up"></div>
  <div class="form-card">
    <h2 class="sec-title"><span class="h-bold">CONTACT</span> <span class="h-light">US</span></h2>
    <div class="field" style="top:112px">Name</div>
    <div class="field" style="top:152px">Email</div>
    <div class="field" style="top:190px">Phone</div>
    <div class="field" style="top:257px">Message</div>
    <div class="btn" style="left:37px;top:314px">Submit now<span class="arrow"><svg width="14" height="14" viewBox="0 0 24 24"><path fill="none" stroke="#1c2b4f" stroke-width="2.5" d="M4 12h15M13 6l6 6-6 6"/></svg></span></div>
  </div>
  <div class="info-box">
    <div class="info-row" style="top:88px"><span class="c"><svg width="14" height="17" viewBox="0 0 24 28"><path fill="#1c2b4f" d="M12 0a10 10 0 00-10 10c0 7.5 10 18 10 18s10-10.5 10-18A10 10 0 0012 0zm0 14a4 4 0 110-8 4 4 0 010 8z"/></svg></span>17 Harrow Street,<br>Westfield, Canada</div>
    <div class="info-row" style="top:166px"><span class="c"><svg width="16" height="16" viewBox="0 0 24 24"><path fill="#1c2b4f" d="M6.6 10.8a15 15 0 006.6 6.6l2.2-2.2a1 1 0 011-.25 11 11 0 003.6.6 1 1 0 011 1V20a1 1 0 01-1 1A17 17 0 013 4a1 1 0 011-1h3.5a1 1 0 011 1 11 11 0 00.6 3.6 1 1 0 01-.25 1z"/></svg></span>(555) 014 2290</div>
    <div class="info-row" style="top:231px"><span class="c"><svg width="16" height="16" viewBox="0 0 24 24" fill="none" stroke="#1c2b4f" stroke-width="2"><rect x="3" y="5" width="18" height="14" rx="1"/><path d="M3 6l9 7 9-7"/></svg></span>hello@korvalbuilds.ca</div>
  </div>
  <div class="tab" style="left:1090px;top:222px;width:45px"></div>
  <div class="tab" style="left:1100px;top:252px;width:35px"></div>
  <div class="tab" style="left:1090px;top:490px;width:60px"></div>
  <div class="tab" style="left:1080px;top:520px;width:45px"></div>
</section>

<section class="section newsletter">
  <h2 class="sec-title"><span class="h-bold">NEWSLETTER</span><br><span class="h-bold">SUBSCRIBE</span> <span class="h-light">NOW</span></h2>
  <div class="sub-box">
    <span class="ph">to get update,enter your email</span>
    <div class="btn">Subscribe now<span class="arrow"><svg width="14" height="14" viewBox="0 0 24 24"><path fill="none" stroke="#1c2b4f" stroke-width="2.5" d="M4 12h15M13 6l6 6-6 6"/></svg></span></div>
  </div>
</section>

<footer class="section footer">
  <div class="logo" style="left:70px;top:120px">
    <span class="mark"></span>
    <div class="name" style="color:#fff"><div style="font-size:18px">KORVAL</div><div style="font-size:18px">RENOVATIONS</div><div style="font-size:8px;letter-spacing:1.8px">AND CUSTOM BUILDS</div></div>
  </div>
  <div class="social"><i></i><i></i><i></i><i></i></div>

  <div class="f-head" style="left:341px">Quick link</div>
  <ul class="f-list" style="left:341px">
    <li>›&nbsp; Home</li><li>›&nbsp; Who we are</li><li>›&nbsp; Services offered</li><li>›&nbsp; Why us</li><li>›&nbsp; Recent projects</li><li>›&nbsp; Gallery</li><li>›&nbsp; Contact us</li>
  </ul>
  <div class="f-head" style="left:587px">Service</div>
  <ul class="f-list" style="left:587px">
    <li>›&nbsp; Finishing basements</li><li>›&nbsp; Second legal units</li><li>›&nbsp; Complete Remodeling</li><li>›&nbsp; Extensions / Additions</li><li>›&nbsp; Kitchen renovations</li><li>›&nbsp; Bathroom Renovations</li><li>›&nbsp; Custom Homes</li><li>›&nbsp; Office and commercial renovations</li>
  </ul>
  <div class="f-head" style="left:857px">Gallery</div>
  <div class="thumb" role="img" aria-label="Project photo: dark kitchen" style="left:859px;top:115px;background:linear-gradient(180deg,#56627a,#1f2733)"></div>
  <div class="thumb" role="img" aria-label="Project photo: bright hallway" style="left:950px;top:115px;background:linear-gradient(180deg,#eeeeee,#6e5848)"></div>
  <div class="thumb" role="img" aria-label="Project photo: basement room" style="left:1041px;top:115px;background:linear-gradient(180deg,#e6e2dc,#8a7a6a)"></div>
  <div class="thumb" role="img" aria-label="Project photo: staircase" style="left:859px;top:189px;background:linear-gradient(180deg,#d2d5d9,#4a5058)"></div>
  <div class="thumb" role="img" aria-label="Project photo: white room" style="left:950px;top:189px;background:linear-gradient(180deg,#f4f4f4,#9fa2a8)"></div>
  <div class="thumb" role="img" aria-label="Project photo: finished corridor" style="left:1041px;top:189px;background:linear-gradient(180deg,#f0ece6,#a39686)"></div>

  <div class="f-line"></div>
  <div class="up"><svg width="14" height="14" viewBox="0 0 24 24" fill="none" stroke="#fff" stroke-width="2.5"><path d="M12 20V5M6 11l6-6 6 6"/></svg></div>
  <div class="copy">Copyright © 2022 <b>KORVALRENOVATIONS</b> All Right Reserved</div>
</footer>

</body>
</html>
```